Custom Beer Labelling Company Needs a Flyer

We need a flyer designed to promote Hopwrapz, a new company in Sydney that helps home brewers create their own small batch beer labels. Main purpose of the flyer is to increase awareness of the service we offer and drive traffic to the Hopwrapz shopify site - www.hopwrapz-example.com.au.
Our value proposition is about being easy (less than 5 minutes), affordable (full set of labels from only $12) with good quality (water resistant synthetic labels that remove cleanly).
The flyer should suit A4 printing and will preferably include screenshot of the "Create your Label" tool on the site, and/or examples of our label templates. It may also include other information from our site such eg from the "About Us" or About Our Labels" pages.

Target Market(s)

Home brewers, mostly males aged 20-50

Industry/Entity Type

It Company

Colors
ec1f27
fee3d4
f9ba93
f68d4e
f37122
f78f20
faa54b
fbc994
ffffff

Requirements
Must have
• Drive customers to www.hopwrapz-example.com as call to action
Nice to have
• screenshot(s) and examples of labels

```html
<!DOCTYPE html>
<html lang="en">
<head>
<meta charset="utf-8">
<title>Hopwrapz Flyer</title>
<link href="https://fonts.googleapis.com/css2?family=Roboto:wght@400;500;700&family=Roboto+Condensed:wght@400;700&display=swap" rel="stylesheet">
<style>
:root{
  --page:#e9e6e1;
  --ink:#1f1a17;
  --brown:#5a3b1a;
  --orange:#f37122;
  --amber:#f78f20;
  --light-amber:#faa54b;
  --straw:#fbc994;
  --cream:#fee3d4;
  --white:#ffffff;
  --red:#ec1f27;
  --wine:#a8243a;
  --bar:#231f20;
}
*{margin:0;padding:0;box-sizing:border-box}
html,body{width:1200px;height:1200px;overflow:hidden;background:var(--page);font-family:"Roboto",sans-serif}
.flyer{position:absolute;left:150px;top:18px;width:953px;height:1233px;transform:scale(0.944);transform-origin:0 0;overflow:hidden;background:var(--white);box-shadow:0 6px 18px rgba(0,0,0,.25)}
.foam{position:absolute;left:0;top:0;width:953px;height:360px;background:linear-gradient(180deg,#fff 0%,#fffaf2 60%,#fde9c8 100%)}
.brand{position:absolute;left:0;top:80px;width:953px;text-align:center}
.brand-row{display:inline-flex;align-items:center;gap:18px}
.brand-square{width:70px;height:70px;background:var(--amber)}
.brand-name{font-weight:700;font-size:96px;color:var(--brown);line-height:1;font-family:"Roboto",sans-serif}
.brand-tag{margin-top:14px;font-weight:700;font-size:27px;letter-spacing:3px;color:var(--brown);font-family:"Roboto",sans-serif}
.intro{position:absolute;left:0;width:953px;top:243px;text-align:center;color:var(--ink)}
.intro-line{font-weight:500;font-size:33px}
.intro-url{font-weight:700;font-size:38px;letter-spacing:4px;margin-top:2px}
.offer-band{position:absolute;left:0;top:350px;width:953px;height:325px;background:linear-gradient(180deg,#fde3b4 0%,var(--light-amber) 25%,var(--amber) 100%)}
.bottle-art{position:absolute;left:55px;top:385px;width:130px;height:270px;border-radius:20px 20px 14px 14px;background:linear-gradient(180deg,#3a2416,#f37122 60%,#3a2416)}
.label-art{position:absolute;left:105px;top:350px;width:195px;height:195px;border-radius:50%;background:radial-gradient(circle,#fff 55%,#f5d6da 100%)}
.offer{position:absolute;left:314px;top:378px;color:var(--ink);font-weight:500;line-height:1.05}
.offer .sm{font-size:33px}
.offer .md{font-size:46px;font-weight:700}
.offer .lg{font-size:66px;font-weight:700}
.slogan{position:absolute;left:195px;top:552px;width:758px;height:55px;background:var(--bar);color:var(--white);font-family:"Roboto Condensed",sans-serif;font-size:35px;line-height:55px;padding-left:115px}
.slogan-under{position:absolute;left:195px;top:605px;width:758px;height:14px}
.feature-band{position:absolute;left:0;top:672px;width:953px;height:240px;background:var(--amber)}
.screenshot{position:absolute;left:58px;top:663px;width:410px;height:278px;background:linear-gradient(180deg,#f2f2f2,#d9d9d9);border:6px solid var(--white);box-shadow:0 6px 10px rgba(0,0,0,.3)}
.features{position:absolute;left:510px;top:693px;width:400px;color:var(--white);font-weight:700;font-size:16.5px;line-height:1.25}
.features p{margin-bottom:20px}
.about-band{position:absolute;left:0;top:912px;width:953px;height:248px;background:linear-gradient(180deg,#fde36a 0%,#fff2a8 60%,#fffbe6 100%)}
.bottles-photo{position:absolute;left:40px;top:985px;width:215px;height:165px;border-radius:6px;background:linear-gradient(180deg,#6b3d1f,#2e1a0e)}
.about{position:absolute;left:285px;top:962px;width:640px;color:var(--ink);font-size:16px;line-height:1.25}
.about p{margin-bottom:8px}
.about .gap{margin-top:20px}
.sizes{color:var(--wine);word-spacing:1px}
.sizes span+span{margin-left:12px}
.footer{position:absolute;left:0;top:1157px;width:953px;height:76px;background:var(--bar);border-top:5px solid var(--orange)}
.footer-cta{position:absolute;left:41px;top:22px;color:var(--light-amber);font-weight:700;font-size:16px}
.footer-url{position:absolute;right:40px;top:10px;color:var(--amber);font-weight:700;font-size:31px}
</style>
</head>
<body>
<main class="flyer">
  <div class="foam"></div>
  <header class="brand">
    <div class="brand-row"><span class="brand-square"></span><span class="brand-name">Hopwrapz</span></div>
    <div class="brand-tag">BEST HOMEBREW LABELS</div>
  </header>
  <section class="intro">
    <div class="intro-line">Easy &amp; affordable small batch beer labels at</div>
    <div class="intro-url">www.hopwrapz-example.com.au</div>
  </section>

  <section class="offer-band"></section>
  <div class="bottle-art" role="img" aria-label="Illustrated beer bottle with custom label"></div>
  <div class="label-art" role="img" aria-label="Example red custom beer label template"></div>
  <div class="offer">
    <div><span class="sm">Less than </span><span class="md">five minutes</span><span class="sm"> and from</span></div>
    <div><span class="lg">just $12</span><span class="sm"> &nbsp;for a full set</span></div>
    <div class="sm" style="font-size:36px">of custom printed labels.</div>
  </div>
  <div class="slogan">Take your homebrew to another level.</div>
  <svg class="slogan-under" viewBox="0 0 758 14" preserveAspectRatio="none"><polygon points="0,0 758,0 758,2 40,14" fill="#a8243a"/></svg>

  <section class="feature-band"></section>
  <div class="screenshot" role="img" aria-label="Screenshot of the Create Your Label tool on the website"></div>
  <div class="features">
    <p>Just fill in template with details of your brew, and select from our range of designs, colours, icons and bottle size.</p>
    <p>We print your labels in high quality LED on A4 sheets of die cut, self-adhesive labels.</p>
    <p>Our synthetic labels are water resistant and remove cleanly from your empties without tearing and without leftover glue crud.</p>
  </div>

  <section class="about-band"></section>
  <div class="bottles-photo" role="img" aria-label="Photo of five homebrew bottles with custom labels"></div>
  <div class="about">
    <p>The team at Hopwrapz have been enthusiastic home brewers for many years. We make some quite drinkable brews that we’re proud to share.</p>
    <p>Our labels are printed on A4 synthetic sheets with adhesive backing. They are strong, water resistant, easy to remove without tearing and without leaving ugly gum residue all over your bottles.</p>
    <p class="gap">We use high quality LED laser printing that’s easy to read and won’t smudge.</p>
    <p class="sizes"><span>Our Small labels (79x68mm, 12 per sheet)</span><span>Our Large labels (99x93mm, 6 per sheet)</span></p>
  </div>

  <footer class="footer">
    <div class="footer-cta">Try a set of Hopwrapz next time you lay down a batch.</div>
    <div class="footer-url">www.hopwrapz-example.com.au</div>
  </footer>
</main>
</body>
</html>
```